The Willowbank Growers Garden Nursery Cards

We are looking for a professional nice business card for the Garden Center. I attached our current cards so you have the information. We do have 2 locations so that is also listed. We like the brown fade in the front, but if you have other ideas that is fine.

Also the back of the card we would like to have the ariel picture of the nursery on the card. I have that picture attached.

I also uploaded our logo files for you.

Target Market(s)

Retail

Industry/Entity Type

Retail Garden Center

Contact Information for Business Card

I have uploaded card samples.

Colors

Designer to choose colors to be used in the design.

Requirements
Must have
• Name, email, phone, cell, locations

```html
<!DOCTYPE html>
<html lang="en">
<head>
<meta charset="utf-8">
<title>The Willowbank Growers – Business Cards</title>
<link href="https://fonts.googleapis.com/css2?family=Cinzel:wght@700&family=Poppins:wght@400;500&display=swap" rel="stylesheet">
<style>
  :root {
    --stage: #2e2e30;
    --brown-deep: #5a2c1c;
    --brown-mid: #7a3f24;
    --glow: #d9925a;
    --cream: #f7efad;
    --gold: #f2d27a;
    --green: #14502a;
    --photo-a: #8d6a4c;
    --photo-b: #a27a56;
    --photo-c: #6f5640;
    --white: #fff8ec;
  }
  * { margin: 0; padding: 0; box-sizing: border-box; }
  html, body { width: 1200px; height: 875px; overflow: hidden; }
  body {
    background: var(--stage);
    display: flex; flex-direction: column; align-items: center;
    justify-content: center; gap: 33px;
    font-family: "Poppins", sans-serif;
  }
  .card {
    position: relative; width: 680px; height: 389px;
    border-radius: 22px; overflow: hidden;
  }
  .card-back .aerial-photo {
    position: absolute; inset: 0;
    background: linear-gradient(135deg, var(--photo-c) 0%, var(--photo-a) 40%, var(--photo-b) 70%, var(--photo-c) 100%);
  }
  .brand {
    position: absolute; display: flex; align-items: center; gap: 14px;
    font-family: "Cinzel", serif; font-weight: 700; color: var(--cream);
    line-height: 1.1;
  }
  .brand-dot { flex: none; border-radius: 50%; background: var(--green); }
  .card-back .brand { left: 50%; top: 50%; transform: translate(-50%, -50%); font-size: 40px; }
  .card-back .brand-dot { width: 64px; height: 64px; }
  .card-front {
    background: radial-gradient(circle at 62% 42%, var(--glow) 0%, var(--brown-mid) 32%, var(--brown-deep) 75%);
  }
  .card-front .wave { position: absolute; inset: 0; width: 100%; height: 100%; }
  .card-front .brand { right: 34px; top: 40px; font-size: 26px; width: 250px; }
  .card-front .brand-dot { width: 46px; height: 46px; }
  .person { position: absolute; left: 44px; top: 96px; color: var(--white); }
  .person-name { font-family: "Cinzel", serif; font-weight: 700; font-size: 30px; color: var(--gold); line-height: 1; }
  .person-role { font-size: 13px; margin-bottom: 12px; }
  .contact-list { list-style: none; font-size: 12.5px; line-height: 1.45; }
  .contact-list li { display: flex; gap: 10px; align-items: flex-start; }
  .contact-list svg { width: 12px; height: 12px; margin-top: 3px; flex: none; fill: var(--cream); }
  .location-name { color: var(--gold); }
  .contact-list .location { margin-top: 6px; }
</style>
</head>
<body>
  <section class="card card-back">
    <div class="aerial-photo" role="img" aria-label="Aerial photograph of the nursery grounds with tree rows, greenhouses and parking, under a warm brown tint"></div>
    <div class="brand"><span class="brand-dot"></span><span>The Willowbank<br>Growers</span></div>
  </section>

  <section class="card card-front">
    <svg class="wave" viewBox="0 0 680 389" preserveAspectRatio="none" aria-hidden="true">
      <path d="M0 352 C300 362 460 350 560 230 C610 172 645 168 680 160 L680 389 L0 389 Z" fill="var(--green)"/>
      <path d="M0 364 C310 374 472 362 572 242 C620 186 650 182 680 176 L680 389 L0 389 Z" fill="var(--cream)"/>
    </svg>
    <div class="brand"><span class="brand-dot"></span><span>The Willowbank Growers</span></div>
    <div class="person">
      <h1 class="person-name">Dale Harmon</h1>
      <p class="person-role">Proprietor</p>
      <ul class="contact-list">
        <li><svg viewBox="0 0 24 24"><path d="M6 2h4l2 5-3 2a12 12 0 0 0 6 6l2-3 5 2v4a2 2 0 0 1-2 2A18 18 0 0 1 4 4a2 2 0 0 1 2-2z"/></svg>386-555-0142</li>
        <li><svg viewBox="0 0 24 24"><path d="M7 1h10a2 2 0 0 1 2 2v18a2 2 0 0 1-2 2H7a2 2 0 0 1-2-2V3a2 2 0 0 1 2-2zm0 3v14h10V4z"/></svg>386-555-0178</li>
        <li><svg viewBox="0 0 24 24"><path d="M2 5h20v14H2zm2 2v.5l8 5 8-5V7z"/></svg>sales@willowbankgrowers.com</li>
        <li><svg viewBox="0 0 24 24"><path d="M12 2a10 10 0 1 0 0 20 10 10 0 0 0 0-20zm0 3a7 7 0 1 1 0 14 7 7 0 0 1 0-14z"/></svg>www.willowbankgrowers.com</li>
        <li class="location"><svg viewBox="0 0 24 24"><path d="M12 1a8 8 0 0 1 8 8c0 6-8 14-8 14S4 15 4 9a8 8 0 0 1 8-8zm0 5a3 3 0 1 0 0 6 3 3 0 0 0 0-6z"/></svg><span><span class="location-name">Maple Crossing</span><br>1420 County Road 9 (Lot 12)</span></li>
        <li class="location"><svg viewBox="0 0 24 24"><path d="M12 1a8 8 0 0 1 8 8c0 6-8 14-8 14S4 15 4 9a8 8 0 0 1 8-8zm0 5a3 3 0 1 0 0 6 3 3 0 0 0 0-6z"/></svg><span><span class="location-name">Cedar Hollow</span><br>2718 Orchard Lane Cedar Hollow FL 30000</span></li>
      </ul>
    </div>
  </section>
</body>
</html>
```